Tess Marlowe Communication business card

I am starting a small, country-based business that offers writing, communication and marketing services to a wide range of clients, inner city big business, to mining, through to agriculture.

The appeal of my business is that it's mobile and flexible. It's just me, with lots of hands-on experience on construction and infrastructure projects.

I can provide the following services:

• Communication planning and management
• Issues and media management
• Marketing and communication materials
• Project management and strategy
• Government liaison
• Incident management communication
• Stakeholder management

It would be great to be able to use the elements of the business card design on other stationery.

Industry/Entity Type

Communication

Requirements
Must have
• The following information:

Tess Marlowe
M: 0427 391 864
E: tess@tmcommsmail.com

PO Box 152
Durrandale Q 4472
Nice to have
• a rural element (windmill, workboots, wheat stalk)

```html
<!DOCTYPE html>
<html lang="en">
<head>
<meta charset="utf-8">
<title>Tess Marlowe Communication – Business Card</title>
<link rel="stylesheet" href="https://fonts.googleapis.com/css2?family=Josefin+Sans:wght@300;400&display=swap">
<style>
  :root {
    --backdrop: #54402f;
    --card-green: #9dca5c;
    --card-green-deep: #8fbf48;
    --brand-green: #93c24c;
    --paper: #ffffff;
    --ink-light: #ffffff;
  }
  * { margin: 0; padding: 0; box-sizing: border-box; }
  html, body {
    width: 1200px; height: 722px; overflow: hidden;
    background: var(--backdrop);
    font-family: "Josefin Sans", sans-serif;
  }
  .canvas { position: relative; width: 1200px; height: 722px; }

  .card {
    position: absolute; top: 110px; width: 301px; height: 527px;
    background: var(--card-green); overflow: hidden;
    box-shadow: 0 4px 14px rgba(0,0,0,.35);
  }
  .card--front { left: 262px; }
  .card--back { left: 613px; }

  .emblem { position: absolute; width: 156px; height: 156px; }
  .card--front .emblem { left: 72px; top: 26px; }
  .card--back .emblem { left: 76px; top: 164px; }

  .name-band {
    position: absolute; left: 0; top: 188px; width: 100%; height: 142px;
    background: var(--paper);
  }
  .grass-strip {
    position: absolute; left: 0; bottom: 0; width: 100%; height: 40px;
    background: linear-gradient(to bottom, var(--paper), #d9ecbd);
  }
  .brand-name {
    position: absolute; left: 0; width: 100%; text-align: center;
    color: var(--brand-green); font-weight: 300; line-height: 1;
  }
  .brand-name--person { top: 18px; font-size: 34px; }
  .brand-name--trade { top: 58px; font-size: 23px; letter-spacing: 1px; }
  .brand-rule {
    position: absolute; left: 20px; right: 20px; top: 86px;
    border-top: 1.5px solid var(--brand-green);
  }

  .contact {
    position: absolute; left: 0; width: 100%; text-align: center;
    color: var(--ink-light); line-height: 1;
  }
  .contact__name { top: 372px; font-size: 22px; letter-spacing: 4px; font-weight: 300; }
  .contact__phone { top: 398px; font-size: 16px; letter-spacing: 4px; font-weight: 300; }
  .contact__email { top: 419px; font-size: 12px; letter-spacing: .5px; }
  .contact__rule {
    position: absolute; left: 76px; width: 150px; top: 447px;
    border-top: 1px solid var(--ink-light);
  }
  .contact__address { top: 468px; font-size: 11px; line-height: 16px; letter-spacing: .5px; }

  .back-name {
    position: absolute; left: 0; width: 100%; text-align: center;
    color: var(--ink-light); font-weight: 300; line-height: 1;
  }
  .back-name--person { top: 324px; font-size: 21px; letter-spacing: 4px; }
  .back-name--trade { top: 348px; font-size: 15px; letter-spacing: 2.5px; }
</style>
</head>
<body>
<main class="canvas">

  <section class="card card--front" aria-label="Business card front">
    <svg class="emblem" viewBox="0 0 156 156" role="img" aria-label="Round emblem area for a windmill illustration">
      <circle cx="78" cy="78" r="76" fill="var(--paper)"/>
      <circle cx="78" cy="78" r="70" fill="var(--card-green-deep)"/>
    </svg>

    <div class="name-band">
      <div class="brand-name brand-name--person">TESS MARLOWE</div>
      <div class="brand-name brand-name--trade">COMMUNICATION</div>
      <div class="brand-rule"></div>
      <div class="grass-strip" role="img" aria-label="Strip for a wild grass illustration"></div>
    </div>

    <div class="contact contact__name">TESS MARLOWE</div>
    <div class="contact contact__phone">0427-391-864</div>
    <div class="contact contact__email">TESS@TMCOMMSMAIL.COM</div>
    <div class="contact__rule"></div>
    <div class="contact contact__address">PO BOX 152<br>DURRANDALE Q 4472</div>
  </section>

  <section class="card card--back" aria-label="Business card back">
    <svg class="emblem" viewBox="0 0 156 156" role="img" aria-label="Round emblem area for a windmill illustration">
      <circle cx="78" cy="78" r="76" fill="var(--paper)"/>
      <circle cx="78" cy="78" r="70" fill="var(--card-green-deep)"/>
    </svg>
    <div class="back-name back-name--person">TESS MARLOWE</div>
    <div class="back-name back-name--trade">COMMUNICATION</div>
  </section>

</main>
</body>
</html>
```